Business Cards for Corvantis LLC

We need business cards for a new company called “Corvantis LLC”. This is a technology process improvement company providing a comprehensive assessment of the technology used to run their business. The documentation and review process delivers the visibility and reassurance they need to protect their business and plan for the future. The product is called “Halvorne Ledgerwork”. Our primary target is small-medium size businesses, with the deliverables going to the decision maker. We would like to see the designs use the color blue. Our tag line is PROTECT YOUR BUSINESS · TAKE CONTROL OF IT.

Industry/Entity Type

Business

Contact Information for Business Card

Tag line should be on back of card - it does not have to be upper case.

Requirements
Must have
• Please use information when laying out card:
• Name: Darnell Pruitt
• Title: Partner
• Phone Number: (877)555-0143
• Email: dell@corvantisllc.com
• Website: http://corvantisllc.com

```html
<!DOCTYPE html>
<html lang="en">
<head>
<meta charset="utf-8">
<title>Corvantis LLC — Business Cards</title>
<link rel="stylesheet" href="https://fonts.googleapis.com/css2?family=Arimo:wght@400;700&display=swap">
<style>
  :root {
    --backdrop: #222325;
    --card-white: #f4f4f4;
    --card-grey: #c9c9c9;
    --card-grey-deep: #9a9a9a;
    --brand-blue: #2a6bb0;
    --brand-blue-light: #5b95cc;
    --ink-light: #ffffff;
    --ink-soft: #dfe8f2;
    --rule-silver: #b3b3b3;
  }
  * { box-sizing: border-box; margin: 0; padding: 0; }
  html, body {
    width: 1200px; height: 890px; overflow: hidden;
    background: var(--backdrop);
    font-family: "Arimo", Arial, sans-serif;
  }
  .canvas {
    width: 1200px; height: 890px;
    display: flex; align-items: center; justify-content: center; gap: 90px;
  }
  .card {
    width: 340px; height: 570px;
    border-radius: 30px;
    overflow: hidden;
    position: relative;
    display: flex; flex-direction: column;
    box-shadow: 0 18px 40px rgba(0,0,0,0.45);
  }

  /* Back of card */
  .card-back .back-panel {
    flex: 0 0 250px;
    background: linear-gradient(160deg, var(--card-grey) 0%, #b5b5b5 100%);
  }
  .card-back .back-field {
    flex: 1;
    background: linear-gradient(180deg, var(--brand-blue) 0%, #24609f 100%);
    display: flex; flex-direction: column; align-items: center; justify-content: flex-end;
    padding-bottom: 70px; text-align: center;
  }
  .tagline-main {
    color: var(--ink-soft);
    font-weight: 700; font-size: 20px; letter-spacing: 0.5px;
  }
  .tagline-sub {
    color: var(--ink-soft);
    font-weight: 400; font-size: 19px; letter-spacing: 0.3px; margin-top: 6px;
  }

  /* Front of card */
  .card-front .front-head {
    flex: 0 0 215px;
    background: var(--card-white);
    display: flex; align-items: center; justify-content: center;
  }
  .wordmark {
    color: var(--brand-blue);
    font-weight: 700; font-size: 34px; letter-spacing: 1px;
  }
  .card-front .front-band {
    flex: 0 0 10px;
    background: var(--card-grey-deep);
  }
  .card-front .front-body {
    flex: 1;
    background: linear-gradient(135deg, var(--brand-blue) 0%, var(--brand-blue) 55%, var(--brand-blue-light) 100%);
    display: flex; flex-direction: column; align-items: center;
    padding-top: 52px; text-align: center; color: var(--ink-light);
  }
  .person-name { font-weight: 700; font-size: 28px; letter-spacing: 1px; }
  .person-title { font-weight: 400; font-size: 21px; margin-top: 6px; }
  .divider { width: 170px; height: 1px; background: var(--ink-soft); margin: 26px 0 24px; opacity: 0.8; }
  .contact-line { font-size: 20px; line-height: 1.5; font-weight: 400; }
</style>
</head>
<body>
  <main class="canvas">
    <section class="card card-back" aria-label="Back of business card">
      <div class="back-panel"></div>
      <div class="back-field">
        <p class="tagline-main">PROTECT YOUR BUSINESS</p>
        <p class="tagline-sub">TAKE CONTROL OF IT</p>
      </div>
    </section>

    <section class="card card-front" aria-label="Front of business card">
      <div class="front-head">
        <span class="wordmark">Corvantis LLC</span>
      </div>
      <div class="front-band"></div>
      <div class="front-body">
        <h1 class="person-name">DARNELL PRUITT</h1>
        <p class="person-title">Partner</p>
        <div class="divider"></div>
        <p class="contact-line">(877)555-0143</p>
        <p class="contact-line">dell@corvantisllc.com</p>
        <p class="contact-line">www.corvantisllc.com</p>
      </div>
    </section>
  </main>
</body>
</html>
```